Real Estate Business Card Redesign Overall - Modern and Clean

Dear All,
I am a real estate Broker in the Texas,USA that has 2 real estate companies that I own. I wanted a clean ,cool modern look on the front with my name and contact info.

The cards can be white or dark color. I plan on using Fipla Print to prin the card in the Luxe Paper. If you think i should rounded corners , i can do that too.

On the back side I wanted to show both my 2 companies somehow.

TORAMIX is a Commercial Real Estate company

KPH uHomes is a Residential Real Estate Company

Target Market(s)

corporate and luxury markets

Industry/Entity Type

Real Estate

Contact Information for Business Card

Marcus T. Holb
Broker or Principal

Marcus T. Holb | CCIM, CPM®, GRI, SRS

address:
4182 Willow Brank Rd Suite 200
Plano, TX 75091 (you can add USA if you want)

Font styles to use
Other font styles liked:
• arial , avantgarde

Colors
0456a4
6092c4
33b8a4
87cfc6
ffffff
474747
5c5c5c
f78f20
ec1f27

Requirements
Must have
• Marcus T. Holb
• address somewhere
• 4182 Willow Brank Rd Suite 200
• Plano, TX 75091
• office phones 555.304.7122
• fax : 555.304.7123
• mobile 555.871.4409
• i have 2 emails:
• marcus@toramix.example
• marcus@kphuhomes.example
• websites:
• www.toramix.example
• www.kphuhomes.example
Nice to have
• Front of the card can be clean with just my name and contact info
• Modern and clean
• On the back we can split the 2 businesses Commercial and Residential

```html
<!DOCTYPE html>
<html lang="en">
<head>
<meta charset="utf-8">
<title>Marcus T. Holb Business Card</title>
<link rel="stylesheet" href="https://fonts.googleapis.com/css2?family=Exo+2:wght@400;500;600&display=swap">
<style>
  :root {
    --page: #ecebe8;
    --card-white: #ffffff;
    --card-shade: #e9e9ea;
    --teal: #22b8b4;
    --grey: #7b7b7d;
    --grey-light: #b9b9bb;
    --ink: #4a4a4c;
  }
  * { box-sizing: border-box; margin: 0; padding: 0; }
  html, body {
    width: 1057px; height: 1200px; overflow: hidden;
    background: var(--page);
    font-family: "Exo 2", Arial, sans-serif;
  }
  .stage { position: relative; width: 1057px; height: 1200px; }
  .card {
    position: absolute; top: 232px;
    width: 420px; height: 735px;
    overflow: hidden;
    background: linear-gradient(160deg, var(--card-white) 30%, var(--card-shade) 100%);
    box-shadow: 0 10px 28px rgba(0,0,0,.18);
  }
  .card--front { left: 80px; }
  .card--back { left: 557px; background: var(--card-white); }
  .card__shape { position: absolute; left: 0; top: 0; width: 420px; height: 735px; }

  .brand {
    position: absolute; top: 60px; left: 56px; right: 40px;
    font-size: 30px; font-weight: 500; color: var(--teal);
    letter-spacing: .5px; white-space: nowrap;
  }
  .brand__sep { color: var(--grey-light); margin: 0 8px; }
  .address {
    position: absolute; top: 118px; left: 56px;
    font-size: 17px; line-height: 24px; color: var(--ink);
  }
  .contacts { position: absolute; top: 192px; left: 56px; list-style: none; }
  .contacts li {
    display: flex; align-items: center; gap: 12px;
    height: 32px; font-size: 14px; color: var(--ink); white-space: nowrap;
  }
  .contacts .label { display: inline-block; width: 52px; color: var(--grey); }
  .contacts .icon {
    width: 20px; height: 20px; border-radius: 4px; flex: none;
    background: var(--grey); display: flex; align-items: center; justify-content: center;
  }
  .contacts .icon--round { border-radius: 50%; }
  .contacts svg { width: 12px; height: 12px; }

  .identity {
    position: absolute; left: 0; width: 420px; top: 636px;
    text-align: center; color: var(--card-white);
  }
  .identity__name { font-size: 24px; font-weight: 500; letter-spacing: 1px; }
  .identity__title { font-size: 16px; letter-spacing: 1.5px; margin-top: 4px; }
  .identity__creds { font-size: 13px; letter-spacing: 1px; margin-top: 4px; }

  .divisions {
    position: absolute; top: 150px; left: 0; width: 420px; height: 300px;
    display: flex;
  }
  .division {
    flex: 1; display: flex; flex-direction: column; align-items: center; justify-content: center;
    color: var(--card-white); text-align: center;
  }
  .division + .division { border-left: 2px solid rgba(255,255,255,.7); }
  .division__name { font-size: 28px; font-weight: 500; letter-spacing: .5px; }
  .division__type { font-size: 14px; letter-spacing: 1.5px; margin-top: 8px; line-height: 20px; }
  .back-web {
    position: absolute; top: 664px; left: 0; width: 420px;
    text-align: center; font-size: 15px; line-height: 24px; color: var(--ink); letter-spacing: .5px;
  }
</style>
</head>
<body>
<main class="stage">

  <section class="card card--front" aria-label="Card front">
    <svg class="card__shape" viewBox="0 0 420 735" aria-hidden="true">
      <path d="M0 560 C120 520 290 525 420 570 L420 590 C290 548 130 548 0 590 Z" fill="var(--grey-light)"/>
      <path d="M0 575 C130 540 300 548 420 598 L420 618 C300 575 140 570 0 612 Z" fill="var(--grey)"/>
      <path d="M0 600 C140 570 300 580 420 628 L420 735 L0 735 Z" fill="var(--teal)"/>
    </svg>

    <div class="brand">TORAMIX<span class="brand__sep">|</span>KPH uHomes</div>
    <p class="address">4182 Willow Brank Rd Suite 200<br>Plano, TX 75091 USA</p>

    <ul class="contacts">
      <li><span class="icon"><svg viewBox="0 0 12 12"><path d="M3 1l2 2-1 1.5a6 6 0 0 0 3.5 3.5L9 7l2 2-1.5 2A9 9 0 0 1 1 2.5Z" fill="#fff"/></svg></span><span class="label">Office</span>555.304.7122</li>
      <li><span class="icon"><svg viewBox="0 0 12 12"><rect x="1" y="4" width="10" height="5" fill="#fff"/><rect x="3" y="1" width="6" height="3" fill="#fff"/></svg></span><span class="label">Fax</span>555.304.7123</li>
      <li><span class="icon"><svg viewBox="0 0 12 12"><rect x="3" y="1" width="6" height="10" rx="1" fill="#fff"/></svg></span><span class="label">Mobile</span>555.871.4409</li>
      <li><span class="icon"><svg viewBox="0 0 12 12"><rect x="1" y="3" width="10" height="7" fill="#fff"/><path d="M1 3l5 4 5-4" stroke="#7b7b7d" fill="none"/></svg></span>marcus@toramix.example</li>
      <li><span class="icon"><svg viewBox="0 0 12 12"><rect x="1" y="3" width="10" height="7" fill="#fff"/><path d="M1 3l5 4 5-4" stroke="#7b7b7d" fill="none"/></svg></span>marcus@kphuhomes.example</li>
      <li><span class="icon icon--round"><svg viewBox="0 0 12 12"><circle cx="6" cy="6" r="4.5" stroke="#fff" fill="none"/><path d="M1.5 6h9M6 1.5v9" stroke="#fff"/></svg></span>www.toramix.example</li>
      <li><span class="icon icon--round"><svg viewBox="0 0 12 12"><circle cx="6" cy="6" r="4.5" stroke="#fff" fill="none"/><path d="M1.5 6h9M6 1.5v9" stroke="#fff"/></svg></span>www.kphuhomes.example</li>
    </ul>

    <div class="identity">
      <p class="identity__name">MARCUS T. HOLB</p>
      <p class="identity__title">BROKER / PRINCIPAL</p>
      <p class="identity__creds">CCIM, CPM®, GRI, SRS</p>
    </div>
  </section>

  <section class="card card--back" aria-label="Card back">
    <svg class="card__shape" viewBox="0 0 420 735" aria-hidden="true">
      <path d="M0 0 H420 V560 C300 535 140 540 0 590 Z" fill="var(--teal)"/>
      <path d="M0 598 C140 550 300 548 420 575 L420 592 C300 568 150 572 0 618 Z" fill="var(--grey)"/>
      <path d="M0 625 C150 582 300 580 420 600 L420 612 C300 596 160 600 0 640 Z" fill="var(--grey-light)"/>
    </svg>
    <div class="divisions">
      <div class="division">
        <p class="division__name">TORAMIX</p>
        <p class="division__type">COMMERCIAL<br>REAL ESTATE</p>
      </div>
      <div class="division">
        <p class="division__name">KPH uHomes</p>
        <p class="division__type">RESIDENTIAL<br>REAL ESTATE</p>
      </div>
    </div>
    <p class="back-web">www.toramix.example<br>www.kphuhomes.example</p>
  </section>

</main>
</body>
</html>
```